Greg wants a Kick arse Business card

Launching my new company Moorvale Real Estate 1st July, and will be mailing out to past clients, need a kick arse business card design pronto to get printing done in time for mail out
I'm after a two sided card - one side for all contact details (see below) the other side for impact (kick arsery!)
Logo and my photo attached, details to go onto card are as follows
Greg Tanbury - Principal
M: 0412 905 327
E: greg@moorvalere.com.au
Greg Tanbury Real Estate Pty Ltd trading as Moorvale Real Estate
Licensed Real Estate & Business Agents
ABN 42 318 507 264 Triennial Cert No. RA31827
14 Banksia Parade, Kelmore WA 6071
Tel: 08 9371 8064 Fax: 08 6250 4718

```html
<!DOCTYPE html>
<html lang="en">
<head>
<meta charset="utf-8">
<title>Moorvale Real Estate — Business Card</title>
<link rel="stylesheet" href="https://fonts.googleapis.com/css2?family=Open+Sans:wght@400;600;700&display=swap">
<style>
  :root {
    --page-bg: #ecedef;
    --blue-deep: #0a4f86;
    --blue-mid: #1479bd;
    --blue-light: #35aee6;
    --panel-white: #ffffff;
    --panel-grey: #dfe3e7;
    --logo-blue: #1a86c7;
    --ink-grey: #6d7780;
    --ink-dark: #2f3a44;
    --text-white: #ffffff;
    --photo-tone-a: #eef0f2;
    --photo-tone-b: #d3d8dc;
    --photo-tone-c: #2d3338;
  }
  * { box-sizing: border-box; margin: 0; padding: 0; }
  html, body {
    width: 1200px; height: 1024px; overflow: hidden;
    background: var(--page-bg);
    font-family: "Open Sans", Arial, sans-serif;
  }
  .sheet {
    width: 1200px; height: 1024px;
    display: flex; flex-direction: column; align-items: center; justify-content: center;
    gap: 28px;
  }
  .card {
    position: relative;
    width: 840px; height: 480px;
    border-radius: 6px;
    overflow: hidden;
    box-shadow: 0 6px 18px rgba(0,0,0,.18);
  }

  /* Front */
  .card-front {
    background:
      radial-gradient(ellipse 60% 70% at 45% 75%, var(--blue-light) 0%, rgba(53,174,230,0) 70%),
      linear-gradient(160deg, var(--blue-deep) 0%, var(--blue-mid) 55%, var(--blue-deep) 100%);
  }
  .front-gloss {
    position: absolute; inset: 0;
    background: linear-gradient(180deg, rgba(255,255,255,.12) 0%, rgba(255,255,255,0) 40%);
  }
  .logo-tab {
    position: absolute; left: 250px; top: 0;
    width: 330px; height: 290px;
    background: linear-gradient(180deg, var(--panel-grey) 0%, var(--panel-white) 45%);
    border-radius: 0 0 165px 165px;
    box-shadow: 0 4px 10px rgba(0,0,0,.25);
    display: flex; flex-direction: column; align-items: center; justify-content: center;
    padding-top: 40px;
  }
  .brand { display: flex; align-items: center; gap: 12px; }
  .brand-dot { width: 34px; height: 34px; border-radius: 50%; background: var(--logo-blue); }
  .brand-name { font-size: 27px; font-weight: 700; color: var(--logo-blue); line-height: 1.1; }
  .brand-tagline { margin-top: 8px; font-size: 11px; letter-spacing: 2px; color: var(--ink-grey); }
  .brand-licence { margin-top: 4px; font-size: 12px; color: var(--ink-grey); }
  .contact-lines {
    position: absolute; right: 40px; bottom: 46px;
    color: var(--text-white);
    font-size: 17px; font-weight: 600;
    display: flex; flex-direction: column; gap: 14px;
  }
  .contact-row { display: flex; justify-content: flex-end; align-items: center; gap: 26px; }
  .contact-item { display: inline-flex; align-items: center; gap: 7px; }
  .contact-item svg { width: 15px; height: 15px; fill: var(--text-white); }

  /* Back */
  .card-back {
    background: linear-gradient(90deg, var(--panel-white) 0%, var(--panel-grey) 100%);
  }
  .portrait {
    position: absolute; right: 60px; top: 30px;
    width: 330px; height: 410px;
    border-radius: 4px;
    background: linear-gradient(180deg, var(--photo-tone-a) 0%, var(--photo-tone-b) 50%, var(--photo-tone-c) 100%);
  }
  .agent {
    position: absolute; left: 60px; top: 110px;
    width: 380px;
  }
  .agent-name {
    font-size: 40px; font-weight: 700; color: var(--logo-blue); line-height: 1.15;
  }
  .agent-title {
    margin-top: 4px;
    font-size: 18px; font-weight: 600; color: var(--ink-grey);
    letter-spacing: 1px; text-transform: uppercase;
  }
  .agent-rule {
    margin: 22px 0; width: 70px; height: 3px; background: var(--logo-blue);
  }
  .agent-contact {
    list-style: none;
    display: flex; flex-direction: column; gap: 12px;
    font-size: 19px; color: var(--ink-dark);
  }
  .agent-contact b { color: var(--logo-blue); font-weight: 700; margin-right: 8px; }
  .back-band {
    position: absolute; left: 0; bottom: 0; width: 100%; height: 40px;
    background: linear-gradient(90deg, var(--blue-deep), var(--blue-mid));
  }
</style>
</head>
<body>
<main class="sheet">

  <section class="card card-front" aria-label="Card front">
    <div class="front-gloss"></div>
    <div class="logo-tab">
      <div class="brand">
        <span class="brand-dot"></span>
        <span class="brand-name">Moorvale<br>Real Estate</span>
      </div>
      <p class="brand-tagline">sales · investing · marketing</p>
      <p class="brand-licence">Licensed Real Estate &amp; Business Agents</p>
    </div>

    <div class="contact-lines">
      <div class="contact-row">
        <span>ABN 42 318 507 264</span>
        <span>Triennial Cert No. RA31827</span>
      </div>
      <div class="contact-row">
        <span class="contact-item">
          <svg viewBox="0 0 24 24" aria-hidden="true"><path d="M12 2a7 7 0 0 0-7 7c0 5 7 13 7 13s7-8 7-13a7 7 0 0 0-7-7zm0 9.5A2.5 2.5 0 1 1 12 6.5a2.5 2.5 0 0 1 0 5z"/></svg>
          14 Banksia Parade, Kelmore WA 6071
        </span>
        <span class="contact-item">
          <svg viewBox="0 0 24 24" aria-hidden="true"><path d="M6.6 10.8a15.1 15.1 0 0 0 6.6 6.6l2.2-2.2a1 1 0 0 1 1-.25 11.4 11.4 0 0 0 3.6.57 1 1 0 0 1 1 1V20a1 1 0 0 1-1 1A17 17 0 0 1 3 4a1 1 0 0 1 1-1h3.5a1 1 0 0 1 1 1c0 1.25.2 2.45.57 3.6a1 1 0 0 1-.25 1z"/></svg>
          08 9371 8064
        </span>
        <span class="contact-item">
          <svg viewBox="0 0 24 24" aria-hidden="true"><rect x="4" y="9" width="16" height="11" rx="2"/><rect x="7" y="3" width="10" height="5" rx="1"/></svg>
          08 6250 4718
        </span>
      </div>
    </div>
  </section>

  <section class="card card-back" aria-label="Card back">
    <div class="agent">
      <h1 class="agent-name">Greg Tanbury</h1>
      <p class="agent-title">Principal</p>
      <div class="agent-rule"></div>
      <ul class="agent-contact">
        <li><b>M:</b>0412 905 327</li>
        <li><b>E:</b>greg@moorvalere.com.au</li>
      </ul>
    </div>
    <div class="portrait" role="img" aria-label="Portrait photograph of Greg Tanbury in a dark jacket on a light backdrop"></div>
    <div class="back-band"></div>
  </section>

</main>
</body>
</html>
```